Audio-Visual & Video Communications Business Requires a Cutting-edge Business Card Design

LinkVessel is a new Audio-Visual & Video Communications company in Cape Town, South Africa that is looking for a cutting-edge business card design. We sell these products to the Corporate, Education & Hospitality markets and will also host an Online Shop for companies and individuals to purchase our products online.

We are already using the following two colours in our logo and draft website. Please incorporate these colours into the design. Please note that our website is still in the design stage if you need to visit it. Green #a0ce4e & Dark Grey #333333.
Updates

Hi,

Please note that I have uploaded our logo in an .eps format.

Target Market(s)

Corporate Companies, Education Institutions & Hospitality Markets

Industry/Entity Type

Business

Requirements
Nice to have
• It would be great if you could incorporate the services that we offer.

1. Consultation & Design
2. Project Management
3. Supply & Installation
4. Onsite Support Personal
5. Online Shop

```html
<!DOCTYPE html>
<html lang="en">
<head>
<meta charset="utf-8">
<title>LinkVessel Business Card</title>
<link rel="stylesheet" href="https://fonts.googleapis.com/css2?family=Open+Sans:wght@400;600;700&display=swap">
<style>
  :root {
    --green: #76b900;
    --grey-dark: #4a4a4a;
    --grey-text: #444444;
    --grey-soft: #a8a8a8;
    --white: #ffffff;
    --page: #ffffff;
  }
  * { margin: 0; padding: 0; box-sizing: border-box; }
  html, body { width: 1200px; height: 900px; overflow: hidden; background: var(--page); }
  body { position: relative; font-family: "Open Sans", Arial, sans-serif; }

  .card {
    position: absolute;
    left: 391px;
    width: 469px;
    height: 286px;
    border-radius: 20px;
    overflow: hidden;
    background: var(--grey-dark);
    box-shadow: 0 10px 22px rgba(0,0,0,0.18);
  }
  .card--front { top: 126px; }
  .card--back { top: 497px; }
  .card__bg { position: absolute; inset: 0; }

  .brand-name {
    position: absolute;
    left: 29px;
    font-size: 25px;
    font-weight: 700;
    color: var(--green);
    letter-spacing: -0.2px;
  }
  .brand-dot {
    position: absolute;
    left: 110px;
    width: 46px;
    height: 46px;
    border-radius: 50%;
    background: var(--green);
  }
  .card--front .brand-name { top: 122px; }
  .card--front .brand-dot { top: 60px; }
  .card--back .brand-name { top: 121px; }
  .card--back .brand-dot { top: 59px; }

  .website {
    position: absolute; left: 29px; top: 168px;
    font-size: 15px; color: var(--grey-text);
  }
  .person {
    position: absolute; right: 17px; top: 135px;
    font-size: 20px; color: var(--white); text-align: right;
  }
  .email {
    position: absolute; right: 17px; top: 175px;
    font-size: 13px; color: var(--green); text-align: right;
  }
  .contact {
    position: absolute; right: 19px; top: 218px;
    font-size: 13px; line-height: 21px; color: var(--grey-text); text-align: right;
  }
  .contact svg { vertical-align: -2px; margin: 0 2px 0 8px; }

  .services {
    position: absolute; left: 301px; top: 155px;
    list-style: none;
    font-size: 11.5px; font-weight: 700; line-height: 21.2px;
    color: var(--grey-soft);
  }
</style>
</head>
<body>

<section class="card card--front" aria-label="Business card front">
  <svg class="card__bg" width="469" height="286" viewBox="0 0 469 286" aria-hidden="true">
    <rect width="469" height="286" fill="var(--grey-dark)"/>
    <circle cx="110" cy="40" r="190" fill="var(--white)"/>
    <rect y="197" width="469" height="89" fill="var(--green)"/>
  </svg>
  <span class="brand-dot" aria-hidden="true"></span>
  <div class="brand-name">LinkVessel</div>
  <div class="website">www.linkvessel.co.za</div>
  <div class="person">Daniel Harte</div>
  <div class="email">me@linkvessel.co.za</div>
  <div class="contact">
    <div>42 Wexley Road • Cape Town - South Africa</div>
    <div>
      <svg width="8" height="13" viewBox="0 0 8 13" aria-hidden="true"><rect x="0.6" y="0.6" width="6.8" height="11.8" rx="1" fill="none" stroke="var(--grey-text)" stroke-width="1.2"/><line x1="3" y1="10.5" x2="5" y2="10.5" stroke="var(--grey-text)"/></svg>+27 82 314-7702
      <svg width="15" height="11" viewBox="0 0 15 11" aria-hidden="true"><path d="M1 4 Q7.5 -1 14 4 L12 5.5 L10 4 L10 3 Q7.5 2 5 3 L5 4 L3 5.5 Z" fill="var(--grey-text)"/><rect x="3" y="6" width="9" height="4.5" rx="1" fill="var(--grey-text)"/></svg>+27 21 460-9315
    </div>
  </div>
</section>

<section class="card card--back" aria-label="Business card back">
  <svg class="card__bg" width="469" height="286" viewBox="0 0 469 286" aria-hidden="true">
    <rect width="469" height="286" fill="var(--grey-dark)"/>
    <circle cx="110" cy="40" r="190" fill="var(--white)"/>
  </svg>
  <span class="brand-dot" aria-hidden="true"></span>
  <div class="brand-name">LinkVessel</div>
  <ul class="services">
    <li>Consultation &amp; Design</li>
    <li>Project Management</li>
    <li>Supply &amp; Installation</li>
    <li>Onsite Support Personal</li>
    <li>Online Shop</li>
  </ul>
</section>

</body>
</html>
```